looking for sleek business card to standout from the crowd!

We are a young biotechnology company looking to help you personalize your health through understanding your genetic make up. We need you help in making a clean but sleek business card design using our new logo. The goal? Any time we give our cards out, people say "nice card!" The feel we are going for is "modern-techy". We don't want to come across as an old, giant pharma company, but not trying to be a hipster either.

Target Market(s)

healthcare and biotechnology industry.

Industry/Entity Type

Biotechnology

Contact Information for Business Card

Info to include on the card will be NAME, TITLE, EMAIL, PHONE. The companies website (www.corvalinbio.com) should also be on the card some where. Would like the logo, when printed, to be raised.

Requirements
Must have
• The logo we have attached in the color it is in. Fonts for text should lean toward more professional/tech.
Nice to have
• Prefer white/light color background
Should not have
• cartoons, landscape backgrounds images.

```html
<!DOCTYPE html>
<html lang="en">
<head>
<meta charset="utf-8">
<title>Corvalin Business Card</title>
<link href="https://fonts.googleapis.com/css2?family=Questrial&display=swap" rel="stylesheet">
<style>
  :root {
    --stage: #2a2a2c;
    --card-white: #f1f1f1;
    --brand-blue: #1f72b6;
    --brand-blue-light: #2a82c4;
    --ink-white: #ffffff;
    --rule-white: rgba(255, 255, 255, 0.35);
  }
  * { margin: 0; padding: 0; box-sizing: border-box; }
  html, body {
    width: 1200px;
    height: 800px;
    overflow: hidden;
    background: var(--stage);
    font-family: "Questrial", "Century Gothic", sans-serif;
  }
  .canvas {
    position: relative;
    width: 1200px;
    height: 800px;
    display: flex;
    align-items: center;
    justify-content: center;
    gap: 60px;
  }
  .card {
    position: relative;
    width: 525px;
    height: 300px;
    border-radius: 18px;
    overflow: hidden;
  }
  .card--front { background: var(--card-white); }
  .card--back {
    background: linear-gradient(160deg, var(--brand-blue-light), var(--brand-blue));
    color: var(--ink-white);
  }
  .edge-bar {
    position: absolute;
    width: 24px;
  }
  .card--front .edge-bar { background: var(--brand-blue); }
  .card--back .edge-bar { background: var(--card-white); }
  .card--front .edge-bar--left { left: 0; top: 40px; height: 110px; }
  .card--front .edge-bar--right { right: 0; top: 165px; height: 110px; }
  .card--back .edge-bar--left { left: 0; top: 30px; height: 135px; }
  .card--back .edge-bar--right { right: 0; top: 125px; height: 135px; }

  .wordmark { letter-spacing: 0.06em; white-space: nowrap; }

  .card--front .wordmark {
    position: absolute;
    left: 50%;
    top: 50%;
    transform: translate(-50%, -50%);
    font-size: 58px;
    color: var(--brand-blue);
  }

  .contact {
    position: absolute;
    inset: 0;
    display: flex;
    flex-direction: column;
    align-items: center;
    text-align: center;
    padding-top: 22px;
  }
  .contact__name { font-size: 22px; letter-spacing: 0.08em; }
  .contact__title { font-size: 14px; letter-spacing: 0.06em; margin-top: 2px; }
  .contact__rule {
    width: 150px;
    height: 1px;
    background: var(--rule-white);
    margin: 9px 0 9px;
  }
  .contact__address { font-size: 18px; letter-spacing: 0.08em; line-height: 1.25; }
  .contact__email { font-size: 16px; letter-spacing: 0.04em; margin-top: 10px; }
  .contact__web { font-size: 19px; letter-spacing: 0.08em; margin-top: 8px; }
  .contact__phone { font-size: 19px; letter-spacing: 0.1em; margin-top: 12px; }
  .card--back .wordmark {
    margin-top: 14px;
    font-size: 24px;
    color: var(--ink-white);
  }
</style>
</head>
<body>
  <main class="canvas">
    <section class="card card--front" aria-label="Card front">
      <span class="edge-bar edge-bar--left"></span>
      <span class="edge-bar edge-bar--right"></span>
      <p class="wordmark">CORVALIN</p>
    </section>

    <section class="card card--back" aria-label="Card back">
      <span class="edge-bar edge-bar--left"></span>
      <span class="edge-bar edge-bar--right"></span>
      <div class="contact">
        <p class="contact__name">Employee Name</p>
        <p class="contact__title">Title</p>
        <span class="contact__rule"></span>
        <p class="contact__address">PO Box 111110, North Street,<br>yourcity 0745</p>
        <p class="contact__email">admin@youremail.com</p>
        <p class="contact__web">www.corvalinbio.com</p>
        <p class="contact__phone">00 123 456 789</p>
        <p class="wordmark">CORVALIN</p>
      </div>
    </section>
  </main>
</body>
</html>
```